Sneaker Company looking for a partner on multiple packaging designs!

We are a company who is passionate about Sneakers and quality products! This project is the first of many packaging designs we will need. We have our logo (see attached) and we would like the background to be all black for this package. I'm working on the UPC number right now so please leave a space for the UPC. Where we need some help is the overall design and some "marketing" word smithing. We are hoping to find a partner that we can work with on future products as well who really understands us and our products! Our company name is Kolvu and this first product will be for crease protection. They are known at Crease Guards, Crease Protection, Anti-Crease Inserts, etc...Not sure the right name to go with but would love some feedback! The package will have 2 Pairs inside. (One Black and One white). This product is something you slide into the shoe while you are wearing it. This product helps prevent the creasing of the toe box. Basically to help keep the sneaker clean and crisp! They are labeled L and R for Left and Right. They are also thin enough that you can trim them with scissors to fit! I have much more to share but before adding all the marketing words, if this is a project you would like to take on please message me and let’s chat! I want to make sure this is a good fit for both of us. Please do not submit projects without speaking to me first. If doing so that means you didn’t read this and you will immediately be removed from contention.

Thank you and look forward to working with you!
Marcus

Target Market(s)

Customers who love Sneakers

Industry/Entity Type

Retail

Font styles to use
Sans Serif

Requirements
Must have
• Clean, Original and Simple
Nice to have
• Pretty open!
Should not have
• Anything copied from another product. No more than 4 colors total on the box.

```html
<!DOCTYPE html>
<html lang="en">
<head>
<meta charset="utf-8">
<title>Kolvu Stride Shield – Box Front and Side</title>
<link rel="stylesheet" href="https://fonts.googleapis.com/css2?family=Exo+2:ital,wght@1,800;1,900&family=Tajawal:wght@500&display=swap">
<style>
  :root {
    --page: #f4f4f4;
    --charcoal: #404145;
    --charcoal-deep: #333438;
    --stone: #dadada;
    --stone-mid: #8d8e91;
    --mint: #2f9e78;
    --white: #ffffff;
  }
  html, body {
    margin: 0;
    width: 1200px;
    height: 1200px;
    overflow: hidden;
    background: var(--page);
  }
  .box-layout {
    position: absolute;
    left: 80px;
    top: 216px;
    width: 1040px;
    height: 768px;
    display: block;
  }
  .bg-stone { fill: var(--stone); }
  .bg-charcoal { fill: var(--charcoal); }
  .band-mid { fill: var(--stone-mid); }
  .band-deep { fill: var(--charcoal-deep); }
  .band-mint { fill: var(--mint); }
  .fold-line { stroke: #c4c4c4; stroke-width: 0.8; }
  .athlete-area { fill: #5a5b5f; opacity: 0.55; }
  .fit-badge { fill: var(--white); stroke: var(--stone-mid); stroke-width: 1.5; }
  .brand-mark { fill: var(--mint); }
  .brand-name {
    font-family: "Tajawal", sans-serif;
    font-weight: 500;
    font-size: 30px;
    letter-spacing: 3px;
    fill: var(--charcoal);
  }
  .brand-name--side { font-size: 20px; letter-spacing: 2px; fill: #d8d8d8; }
  .product-title {
    font-family: "Exo 2", sans-serif;
    font-style: italic;
    font-weight: 900;
    font-size: 44px;
    fill: #ececec;
  }
  .product-title--side { font-size: 22px; fill: var(--charcoal-deep); }
  .product-subtitle {
    font-family: "Tajawal", sans-serif;
    font-weight: 500;
    font-size: 22px;
    fill: var(--mint);
  }
  .product-subtitle--side { font-size: 12px; }
  .tagline {
    font-family: "Exo 2", sans-serif;
    font-style: italic;
    font-weight: 800;
    font-size: 24px;
    fill: #f2f2f2;
  }
  .size-label {
    font-family: "Exo 2", sans-serif;
    font-style: italic;
    font-weight: 900;
    font-size: 24px;
    fill: var(--charcoal-deep);
  }
  .sneaker-area { fill: url(#sneakerTone); stroke: #bdbdbd; stroke-width: 1; }
</style>
</head>
<body>
<svg class="box-layout" viewBox="0 0 690 510" xmlns="http://www.w3.org/2000/svg">
  <defs>
    <linearGradient id="sneakerTone" x1="0" y1="0" x2="0" y2="1">
      <stop offset="0" stop-color="#f1f1f1"/>
      <stop offset="0.7" stop-color="#e4e4e4"/>
      <stop offset="1" stop-color="#cfcfcf"/>
    </linearGradient>
  </defs>

  <!-- Front face -->
  <g class="panel-front">
    <rect class="bg-stone" width="690" height="398"/>
    <polygon class="bg-charcoal" points="0,0 268,0 480,212 300,398 0,398"/>
    <polygon class="band-mid" points="268,0 292,0 500,212 480,212"/>
    <polygon class="band-mid" points="238,398 320,318 348,318 268,398"/>
    <polygon class="band-deep" points="590,160 690,60 690,260"/>
    <polygon class="band-mint" points="550,120 610,60 690,140 630,200"/>
    <polygon class="band-mint" points="410,398 690,160 690,398"/>

    <rect class="athlete-area" x="70" y="30" width="170" height="340" rx="60"
          role="img" aria-label="Faint silhouette of a basketball player dribbling"/>

    <circle class="fit-badge" cx="58" cy="58" r="30"
            role="img" aria-label="Universal fit badge"/>

    <rect class="brand-mark" x="456" y="26" width="14" height="14"/>
    <text class="brand-name" x="463" y="82" text-anchor="middle">Kolvu</text>

    <text class="product-title" x="12" y="134">STRIDE</text>
    <text class="product-title" x="12" y="180">SHIELD</text>
    <text class="product-subtitle" x="14" y="214">Anti-Crease Inserts</text>

    <text class="tagline" x="12" y="274">Designed</text>
    <text class="tagline" x="8" y="304">for Maximum</text>
    <text class="tagline" x="4" y="334">Comfort</text>

    <rect class="sneaker-area" x="252" y="155" width="420" height="210" rx="40"
          role="img" aria-label="Line drawing of a high-top sneaker fitted with a black anti-crease insert at the toe box"/>

    <text class="size-label" x="580" y="392">LARGE</text>
  </g>

  <!-- Side face -->
  <g class="panel-side">
    <rect class="bg-stone" x="0" y="398" width="690" height="112"/>
    <polygon class="bg-charcoal" points="0,398 300,398 220,510 0,510"/>
    <polygon class="band-deep" points="330,398 356,398 276,510 250,510"/>
    <line class="fold-line" x1="0" y1="398" x2="690" y2="398"/>

    <rect class="brand-mark" x="26" y="430" width="10" height="10"/>
    <text class="brand-name brand-name--side" x="44" y="442">Kolvu</text>

    <text class="product-title product-title--side" x="640" y="434" text-anchor="end">STRIDE</text>
    <text class="product-title product-title--side" x="640" y="456" text-anchor="end">SHIELD</text>
    <text class="product-subtitle product-subtitle--side" x="640" y="472" text-anchor="end">Anti-Crease Inserts</text>
  </g>
</svg>
</body>
</html>
```